Clean Chic Simple Black & White One sided Biz Card

I need a business card for my company Brightwater Docket Partners. We are a luxury, white glove service for organizing files for attorneys.
I would like something that is stunningly simple and chic/sexy. This is going to be only one sided. We are going to use raised ink or ink embossing for the printing. So the logo will be raised in black. I am currently waiting to hear back from the printer as to whether or not the logo has to be in all black or can be left in its current state of black with grey initials. Please check our website for inspiration. www.brightwaterdocketpartners.example.
Thank you so much for your time.

* Please decide whichever title you think looks best(Chief Executive Officer, CEO, or President)
Updates

I really like the designs that make the logo large and the main focus.  
I also like the use of modern, masculine, simple, chic fonts for the slogan and info.

1) No bold font on slogan or info
2) Shrink info to be smaller maybe to make the logo bigger and more the focus
3) Maybe use grey for all the info and slogan so the focus will be on the logo

Thank you so much for your time!!

Target Market(s)

Luxury driven lawyers and their support staff

Industry/Entity Type

Printer

Requirements
Must have
• One sided card

Modern, sleek, masculine, chic, simple font.

Please add our slogan. Refer to file labeled "old logo" to see how we added our slogan under the old logo.
The slogan is, "Every Case File, Calmly in Order"

Please include the info below:
Marina Thornbury (Chief Executive Officer, CEO, or President)
812 North Delmont Avenue, Suite 1400
Los Angeles, California 90017
P: (213)555-0186 F: (213)555-0142
marinat@brightwaterdocketpartners.example
www.brightwaterdocketpartners.example

Please refer to attached file labeled "inkpressingembossing requirements" for requirements from my printer. Thank you!
Nice to have
• It can be super simple with just the logo and my info. Or it could maybe have some cool feature. Just clean please.

I would prefer the info not be in bold. I think this will help the Logo stand out as the main focus.

I attached files of how the ink pressing and embossing will look.
Should not have
• No crazy shapes and no color other than black with a white background. The logo should be the focus since it will be embossed.

```html
<!DOCTYPE html>
<html lang="en">
<head>
<meta charset="utf-8">
<title>Brightwater Docket Partners — Business Card</title>
<link rel="stylesheet" href="https://fonts.googleapis.com/css2?family=Cabin:wght@400&family=Tinos:ital,wght@0,700;1,400&display=swap">
<style>
  :root {
    --backdrop: #2a2a2a;
    --card: #ffffff;
    --ink: #111111;
    --mark-grey: #b4b4b4;
    --slogan-grey: #666666;
    --info-grey: #4a4a4a;
    --name-grey: #3a3a3a;
    --rule: #555555;
  }
  * { margin: 0; padding: 0; box-sizing: border-box; }
  html, body {
    width: 1200px; height: 900px; overflow: hidden;
    background: var(--backdrop);
  }
  .card {
    position: absolute;
    left: 100px; top: 163px;
    width: 1000px; height: 575px;
    background: var(--card);
    box-shadow: 0 6px 18px rgba(0,0,0,0.45);
  }
  .brand-dot {
    position: absolute;
    left: 430px; top: 64px;
    width: 140px; height: 140px;
    border-radius: 50%;
    border: 6px solid var(--mark-grey);
  }
  .brand-name {
    position: absolute;
    left: 0; right: 0; top: 222px;
    text-align: center;
    font-family: "Tinos", serif;
    font-weight: 700;
    font-size: 31px;
    letter-spacing: 5px;
    color: var(--ink);
    text-transform: uppercase;
    white-space: nowrap;
  }
  .slogan {
    position: absolute;
    left: 0; right: 0; top: 278px;
    text-align: center;
    font-family: "Tinos", serif;
    font-style: italic;
    font-size: 26px;
    color: var(--slogan-grey);
  }
  .info {
    font-family: "Cabin", sans-serif;
    font-weight: 400;
    color: var(--info-grey);
    white-space: nowrap;
  }
  .contact-person {
    position: absolute; left: 66px; top: 374px;
  }
  .person-name { font-size: 29px; line-height: 36px; color: var(--name-grey); text-transform: uppercase; }
  .person-title { font-size: 20px; line-height: 32px; }
  .person-online { margin-top: 16px; font-size: 18.5px; line-height: 29px; }
  .divider {
    position: absolute; left: 476px; top: 379px;
    width: 2px; height: 142px;
    background: var(--rule);
  }
  .contact-office {
    position: absolute; left: 545px; top: 380px;
    font-size: 20px; line-height: 33px;
  }
  .office-address { margin-top: 16px; line-height: 29px; }
</style>
</head>
<body>
  <main class="card">
    <div class="brand-dot" aria-hidden="true"></div>
    <h1 class="brand-name">Brightwater Docket Partners, Inc.</h1>
    <p class="slogan">“Every Case File, Calmly in Order”</p>

    <section class="contact-person info">
      <p class="person-name">Marina Thornbury</p>
      <p class="person-title">Chief Executive Officer</p>
      <div class="person-online">
        <p>marinat@brightwaterdocketpartners.example</p>
        <p>www.brightwaterdocketpartners.example</p>
      </div>
    </section>

    <div class="divider" aria-hidden="true"></div>

    <section class="contact-office info">
      <p>P: (213) 555-0186</p>
      <p>F: (213) 555-0142</p>
      <div class="office-address">
        <p>812 North Delmont Avenue, Suite 1400</p>
        <p>Los Angeles, California 90017</p>
      </div>
    </section>
  </main>
</body>
</html>
```